Bluvora business website

I am wanting a website for my media agency Bluvora.

It needs to be be an attractive, unique and professional looking website. The website is a destination for people to be able to understand the service that Bluvora offers.

Please read uploaded website copy to gain an understanding of the business.

Target Market(s)

small business owners, business decision makers, marketing managers,

Industry/Entity Type

Business

Requirements
Must have
• Good branding.

```html
<!DOCTYPE html>
<html lang="en">
<head>
<meta charset="utf-8">
<title>Bluvora — media agency</title>
<link href="https://fonts.googleapis.com/css2?family=Questrial&family=Noto+Sans:wght@400;700&display=swap" rel="stylesheet">
<style>
  :root {
    --brand: #3d4a9c;
    --brand-dark: #2e3880;
    --page: #dcdedf;
    --band: #cfd2d3;
    --ink: #555a60;
    --heading: #4a4f55;
    --rule: #b6babd;
    --teal: #5b9f9a;
    --olive: #a3ad5c;
    --rose: #d48c92;
    --footer: #474747;
    --footer-ink: #d8d8d8;
    --white: #ffffff;
  }
  * { margin: 0; padding: 0; box-sizing: border-box; }
  html, body { width: 712px; height: 1200px; overflow: hidden; }
  body {
    position: relative;
    background: linear-gradient(160deg, #e4e6e7 0%, var(--page) 45%, #d6d9da 100%);
    font-family: "Noto Sans", Tahoma, sans-serif;
    color: var(--ink);
  }
  h2, h3, h4 { font-weight: 400; }
  .abs { position: absolute; }

  .top-rule { left: 0; top: 0; width: 712px; height: 3px; background: var(--brand); }

  .brand { left: 38px; top: 30px; display: flex; align-items: center; gap: 6px; }
  .brand-square { width: 14px; height: 14px; background: var(--brand); }
  .brand-name { font-family: "Noto Sans", sans-serif; font-size: 19px; font-weight: 700; color: var(--brand); line-height: 1; }

  .phone { left: 570px; top: 20px; font-size: 8px; color: #5b6066; display: flex; align-items: center; gap: 3px; }
  .search { left: 566px; top: 48px; width: 104px; height: 13px; background: var(--white);
    border-radius: 7px; font-size: 7.5px; color: #b5b8bb; padding: 1px 6px; }
  .search svg { position: absolute; right: 5px; top: 3px; }

  .nav { left: 345px; top: 72px; width: 367px; height: 22px; background: var(--brand);
    clip-path: polygon(14px 0, 100% 0, 100% 100%, 0 100%); }
  .nav ul { list-style: none; display: flex; gap: 14px; position: absolute; left: 27px; top: 4px; }
  .nav li { font-size: 9.2px; color: var(--white); }
  .header-shadow { left: 0; top: 88px; width: 352px; height: 6px; background: linear-gradient(180deg, #c2c4c6, #9da0a3); }

  .hero { left: 0; top: 94px; width: 712px; height: 252px;
    background: linear-gradient(100deg, #1d2a3d 0%, #3f5570 30%, #c9d3dc 50%, #4b6079 68%, #9aa9b8 88%, #56667a 100%); }
  .hero-arrow { top: 189px; width: 30px; height: 30px; border-radius: 50%; background: rgba(200,204,208,.6); }
  .hero-caption { left: 0; top: 291px; width: 712px; height: 55px; background: rgba(20,24,32,.55); }
  .hero-text { left: 72px; top: 302px; width: 332px; font-size: 6.9px; line-height: 10px; color: var(--white); text-align: justify; }
  .hero-button { left: 436px; top: 306px; width: 85px; height: 26px; background: var(--brand-dark);
    color: var(--white); font-family: "Questrial", sans-serif; font-size: 11.5px; line-height: 26px; text-align: center; }

  .section-title { left: 160px; font-family: "Questrial", sans-serif; font-size: 16.5px; color: var(--heading); }
  .section-rule { left: 160px; width: 403px; height: 1px; background: var(--rule); }
  .about-copy { left: 163px; top: 405px; width: 402px; font-size: 7.4px; line-height: 13.3px; color: #666b70; }

  .band { left: 0; width: 712px; background: rgba(170,176,180,.22); }

  .service-photo { width: 116px; height: 116px; border-radius: 50%; border: 1px dashed #a9adb0;
    background: #e9eaeb; padding: 6px; }
  .service-photo div { width: 100%; height: 100%; border-radius: 50%; }
  .service-title { font-family: "Questrial", sans-serif; font-size: 13px; }
  .service-copy { font-size: 7.4px; line-height: 13.3px; color: #7a7f84; }

  .divider { left: 163px; width: 404px; height: 1px; background: var(--rule); }
  .divider-dot { width: 8px; height: 8px; border-radius: 50%; }

  .footer { left: 0; top: 1064px; width: 712px; height: 136px; background: var(--footer); }
  .footer-title { font-family: "Questrial", sans-serif; font-size: 10.5px; color: var(--white); }
  .quicklinks { left: 120px; top: 1098px; display: grid; grid-template-columns: 64px 60px; row-gap: 3px; font-size: 7.8px; color: var(--footer-ink); }
  .social { top: 1154px; width: 19px; height: 19px; border-radius: 50%; }
  .field { left: 297px; width: 91px; height: 17px; background: #f0f0f0; border: 1px solid #cfcfcf;
    font-size: 7.2px; color: #8a8a8a; padding: 3px 5px; }
  .subscribe { left: 297px; top: 1143px; width: 45px; height: 15px; background: #6a6a6a; color: var(--white);
    font-size: 7.2px; line-height: 15px; text-align: center; }
  .map { left: 468px; top: 1075px; width: 207px; height: 107px; border: 3px solid var(--white);
    background: linear-gradient(135deg, #e4e2dc 0%, #ecebe6 55%, #b9cfe0 100%); }
  .copyright { right: 37px; top: 1187px; font-size: 7.2px; color: var(--footer-ink); }
</style>
</head>
<body>
  <div class="abs top-rule"></div>

  <header>
    <div class="abs brand"><span class="brand-square"></span><span class="brand-name">Bluvora</span></div>

    <div class="abs phone">
      <svg width="7" height="8" viewBox="0 0 7 8"><path d="M1.5 0.5 L3 2.2 L2.2 3.2 Q3 4.8 4.3 5.6 L5.2 4.8 L6.7 6.3 L5.7 7.5 Q2.5 7 0.5 1.5 Z" fill="#5b6066"/></svg>
      Call us 555-0142-778
    </div>
    <div class="abs search">Search
      <svg width="7" height="7" viewBox="0 0 7 7"><circle cx="2.8" cy="2.8" r="2" fill="none" stroke="#b5b8bb" stroke-width="1"/><line x1="4.3" y1="4.3" x2="6.5" y2="6.5" stroke="#b5b8bb" stroke-width="1.2"/></svg>
    </div>

    <div class="abs header-shadow"></div>
    <nav class="abs nav">
      <ul>
        <li>Home</li><li>About</li><li>What We Do</li><li>People</li><li>Ideas</li><li>Contact Us</li>
      </ul>
    </nav>
  </header>

  <section>
    <div class="abs hero" role="img" aria-label="Upward view of glass office towers against a pale sky"></div>
    <div class="abs hero-arrow" style="left:13px"><svg width="30" height="30" viewBox="0 0 30 30"><path d="M19 8 L9 15 L19 22 Z" fill="#4a4f55"/></svg></div>
    <div class="abs hero-arrow" style="left:667px"><svg width="30" height="30" viewBox="0 0 30 30"><path d="M11 8 L21 15 L11 22 Z" fill="#4a4f55"/></svg></div>
    <div class="abs hero-caption"></div>
    <p class="abs hero-text">Lorem ipsum dolor sit amet, consectetur adipiscing elit. Nam hendrerit ornare pellentesque. Sed nec dolor eleifend, condimentum massa in, commodo nibh. Vivamus eget metus ut magna rutrum mollis. Aliquam nec interdum urna. Phasellus laoreet dictum tellus in molestie.</p>
    <div class="abs hero-button">Learn more</div>
  </section>

  <section>
    <h2 class="abs section-title" style="top:364px">About us</h2>
    <div class="abs section-rule" style="top:388px"></div>
    <p class="abs about-copy">Bluvora is a media strategy, planning and buying agency. We work with both small and big businesses. Bluvora works across all offline platforms (radio, press, outdoor &amp; TV), search engine marketing, online display, email, social &amp; mobile. We attain a high level of value for our clients with a focus on integration. We are marketing partners in our clients businesses and enjoy seeing them grow and achieve their goals.</p>
  </section>

  <section>
    <h2 class="abs section-title" style="top:489px">What We Do</h2>
    <div class="abs band" style="top:512px;height:170px"></div>
    <div class="abs section-rule" style="top:512px"></div>

    <div class="abs service-photo" style="left:155px;top:529px"><div role="img" aria-label="Hands working over charts and coffee cups on a desk" style="background:linear-gradient(135deg,#f2f3f6,#b9bfd0)"></div></div>
    <h3 class="abs service-title" style="left:308px;top:536px;color:var(--teal)">Media Strategy &amp; Planning</h3>
    <p class="abs service-copy" style="left:310px;top:559px;width:258px">Using accurate analysis we provide relevant research about the consumer or business target &amp; trends in the market place. A tailored strategy is devised that comprises of the right media channels that fit with the target &amp; business network. Thorough and insightful planning ensures each media channel is utilized correctly and market opportunities are maximized.</p>

    <div class="abs divider" style="top:682px"></div>
    <div class="abs divider-dot" style="left:361px;top:678px;background:var(--olive)"></div>

    <h3 class="abs service-title" style="left:164px;top:703px;color:var(--olive)">Media Training &amp; Campaign Monitoring</h3>
    <p class="abs service-copy" style="left:165px;top:726px;width:262px">Using our media partner relationships, trade negotiation techniques &amp; experience we achieve a high level of value for all media buys that leads to significant cost savings for clients.<br><br>All media activity is monitored &amp; optimized to ensure performance.</p>
    <div class="abs service-photo" style="left:455px;top:698px"><div role="img" aria-label="Black and white photo of a team meeting in an office" style="background:linear-gradient(135deg,#d8d8d8,#5c5c5c)"></div></div>

    <div class="abs band" style="top:839px;height:170px"></div>
    <div class="abs divider" style="top:839px"></div>
    <div class="abs divider-dot" style="left:361px;top:835px;background:var(--rose)"></div>

    <div class="abs service-photo" style="left:155px;top:858px"><div role="img" aria-label="Hand touching a glowing network of contact icons" style="background:radial-gradient(circle at 45% 40%,#c7c9e6,#5a5f95 60%,#2d2f55)"></div></div>
    <h3 class="abs service-title" style="left:308px;top:866px;color:var(--rose)">Content &amp; Creative</h3>
    <p class="abs service-copy" style="left:310px;top:889px;width:258px">Creating imaginative &amp; interesting content for a brand can be a great way of achieving a high level of engagement to a target audience. Content can be published and broadcast on a variety of different media platforms.<br>We also have a network of creative contacts that will happily create awesome ads across all formats.</p>
  </section>

  <footer>
    <div class="abs footer"></div>
    <h4 class="abs footer-title" style="left:118px;top:1075px">Quicklinks</h4>
    <div class="abs quicklinks">
      <span>Home</span><span>People</span>
      <span>About</span><span>Ideas</span>
      <span>What We Do</span><span>Contat us</span>
    </div>
    <div class="abs social" style="left:120px;background:#55aedc" aria-label="Social link"></div>
    <div class="abs social" style="left:146px;background:#d8555c" aria-label="Social link"></div>
    <div class="abs social" style="left:171px;background:#4a69ad" aria-label="Social link"></div>
    <div class="abs social" style="left:196px;background:#3a84bf" aria-label="Social link"></div>

    <h4 class="abs footer-title" style="left:297px;top:1075px">Newsletter</h4>
    <div class="abs field" style="top:1098px">Your Name</div>
    <div class="abs field" style="top:1119px">your@email.com</div>
    <div class="abs subscribe">Subscribe</div>

    <div class="abs map" role="img" aria-label="Street map showing the office location"></div>
    <p class="abs copyright">Bluvora 2013 Copyright All rights reserved.</p>
  </footer>
</body>
</html>
```